iOS developer portal page

We need a web design for a company based in Beijing called BrightNook. Our company develops an SDK used by iOS developers making children's educational apps. The SDK provides cross-promotional marketing, user analytics, teacher feedback and activities, and parent reports for developers who implement it.
Our company offers a product that benefits parents and developers, however the design we need is in regard to the landing page for developers using our product.Developers using our SDK are mostly based in the USA and develop apps for the USA Orchard Tunebox store.
There is an included wireframe for the first design idea. Design comps can be similar or different from the wireframe, however it should be considered as a good starting point for the final design.
Updates
Thank you for the design submissions. We are currently reviewing the designs internally and will notify all designers once a decision has been reached.
Kind regards,
Merrick
Project Deadline Extended
Reason: The deadline is being extended by one day so it will be closed at the end of the business week. Thank you.
Target Market(s)
iOS Developers for Children's education apps
Industry/Entity Type
It Company
Look and feel
Each slider illustrates characteristics of the customer's brand and the style your logo design should communicate.

```html
<!DOCTYPE html>
<html lang="en">
<head>
<meta charset="utf-8">
<title>BrightNook – Developer Portal</title>
<link rel="stylesheet" href="https://fonts.googleapis.com/css2?family=Cinzel:wght@400;700&family=Questrial&family=Arimo:wght@400;700&family=Tinos:ital@1&display=swap">
<style>
:root{
  --page:#f3f7f7;
  --white:#ffffff;
  --nav-text:#3b4a5a;
  --heading-red:#8e1a12;
  --navy:#0f2a47;
  --body-grey:#555555;
  --title-grey:#333333;
  --green:#5fc01e;
  --green-dark:#46a012;
  --btn-grey-text:#777777;
  --border:#dddddd;
  --footer-text:#888888;
  --sign-dark:#1e1e1e;
}
*{box-sizing:border-box;margin:0;padding:0}
html,body{width:943px;height:1200px;overflow:hidden;background:var(--page)}
body{position:relative;font-family:"Arimo",Arial,sans-serif;color:var(--body-grey)}
.abs{position:absolute}
.topbar{left:0;top:0;width:943px;height:40px;background:linear-gradient(#ffffff,#ececec);border-bottom:1px solid #d8d8d8}
.topbar a{position:absolute;top:11px;font-family:"Cinzel",serif;font-size:15px;letter-spacing:1.5px;color:var(--nav-text);text-decoration:none}
.hero{left:0;top:40px;width:943px;height:466px;background:linear-gradient(180deg,#cfe7ee 0%,#b9dbe3 45%,#b48a5e 70%,#8a6440 100%)}
.hero-photo{left:330px;top:40px;width:613px;height:370px;background:radial-gradient(ellipse at 60% 55%,#c0392b 0%,#b5463c 25%,rgba(185,219,227,0) 60%)}
.brand{left:56px;top:76px;display:flex;align-items:center;gap:10px;font-family:"Questrial",sans-serif;font-size:38px;color:#5aa81c}
.brand i{display:block;width:26px;height:26px;border-radius:50%;background:#f0a21c}
.intro{left:42px;top:164px;width:353px;height:155px;background:rgba(255,255,255,.82);padding:8px 14px}
.intro h1{font-family:"Cinzel",serif;font-weight:700;font-size:29px;line-height:31px;color:var(--heading-red);letter-spacing:.5px}
.intro p{margin-top:6px;font-size:11px;line-height:17px;color:#555}
.signup{left:93px;top:340px;width:173px;height:41px;border-radius:4px;background:linear-gradient(#4a4a4a,var(--sign-dark));color:#eee;font-family:"Cinzel",serif;font-size:22px;letter-spacing:2px;text-align:center;line-height:41px}
.panel{background:var(--white);border:1px solid var(--border);box-shadow:0 1px 3px rgba(0,0,0,.08)}
.features{left:42px;top:413px;width:859px;height:385px}
.features h2{position:absolute;left:0;top:10px;width:100%;text-align:center;font-family:"Questrial",sans-serif;font-weight:400;font-size:40px;color:var(--navy)}
.feature{position:absolute;top:73px;width:195px}
.feature .thumb{width:195px;height:110px;border:1px solid #ccc}
.feature h3{margin-top:10px;height:48px;font-family:"Questrial",sans-serif;font-weight:400;font-size:21px;line-height:21px;color:var(--title-grey)}
.feature p{margin-top:4px;font-size:11px;line-height:18px;color:#666;padding-right:10px}
.more{position:absolute;top:344px;width:159px;height:24px;border-radius:3px;background:linear-gradient(#f2f2f2,#dcdcdc);color:var(--btn-grey-text);font-size:12px;font-weight:700;line-height:24px;padding:0 18px;display:flex;justify-content:space-between}
.more.primary{background:linear-gradient(var(--green),var(--green-dark));color:#fff}
.box{top:832px;width:347px;height:140px}
.feature-box{left:77px}
.testimonial{left:514px}
.box .pic{position:absolute;left:15px;top:17px;width:105px;height:105px}
.box h4{position:absolute;top:16px;font-family:"Arimo",sans-serif;font-weight:400;font-size:16px;line-height:20px;color:var(--title-grey)}
.feature-box .logo-slot{position:absolute;left:15px;top:17px;width:144px;height:105px;border:1px solid #ccc;font-family:"Arimo",sans-serif;font-size:17px;color:#2a9d2a;display:flex;align-items:center;justify-content:center}
.feature-box h4{left:170px;width:165px}
.feature-box p{position:absolute;left:170px;top:62px;width:170px;font-size:11px;line-height:17px;color:#666}
.testimonial h4{left:138px}
.testimonial blockquote{position:absolute;left:138px;top:40px;width:195px;font-family:"Tinos",serif;font-style:italic;font-size:13px;line-height:18px;color:#666}
.testimonial cite{position:absolute;right:15px;top:118px;font-style:normal;font-size:11px;font-weight:700;color:var(--green)}
.apps{left:42px;top:1005px;width:859px;height:129px}
.app{position:absolute;top:32px;display:flex;gap:14px}
.app .icon{width:74px;height:74px;border-radius:14px}
.app b{display:block;font-size:16px;color:#111;margin-top:6px}
.app span{display:block;font-size:16px;line-height:20px;color:#222}
.arrow{position:absolute;top:50px}
.footer{left:57px;top:1150px;font-size:11px;color:var(--footer-text);letter-spacing:.5px}
.social{top:1143px;width:28px;height:28px;border-radius:3px}
</style>
</head>
<body>
<nav class="abs topbar">
  <a style="left:438px">ABOUT</a>
  <a style="left:533px">NEWS</a>
  <a style="left:617px">SUPPORT</a>
  <a style="left:728px">CONTACT</a>
  <a style="left:834px">LOGIN</a>
</nav>

<section class="abs hero" role="img" aria-label="Photo of a boy in a red shirt lying on a wooden floor using a laptop"></section>
<div class="abs hero-photo" aria-hidden="true"></div>

<div class="abs brand"><i></i>BrightNook</div>

<div class="abs intro">
  <h1>MAKE YOUR APP'S IRRESISTABLE</h1>
  <p>Lorem ipsum dolor sit asectetuer adipiscing elit. Aenean ommodligula eget dolor. Aeassa. C sociiss natoque penatibu-
  Lorem ipsum dolor sit asectetuer adipiscing elit. Aenean ommodligula eget dolor. Aeassa. C sociiss natoque penatibu</p>
</div>
<div class="abs signup">SIGN UP</div>

<section class="abs panel features">
  <h2>Enable These Great Featured in Minutes!</h2>
  <div class="feature" style="left:17px">
    <div class="thumb" role="img" aria-label="Photo of a smiling schoolboy holding a graded paper" style="background:linear-gradient(90deg,#e6e2dc,#d65a2a 50%,#e9e5df)"></div>
    <h3>Parent Report</h3>
    <p>Lorem ipsum dolor sit amet,sectetuer adipiscing elit. Aenean commodligula eget dolor. Aenean massa. C sociiss natoque penatibus et magn dis parturient montes,</p>
  </div>
  <div class="feature" style="left:228px">
    <div class="thumb" role="img" aria-label="Collage of marketing words with a globe" style="background:linear-gradient(120deg,#2c4f78,#dfe6ee 55%,#f4f4f4)"></div>
    <h3>Cross-promotional Marketing</h3>
    <p>Lorem ipsum dolor sit amet,sectetuer adipiscing elit. Aenean commodligula eget dolor. Aenean massa. C sociiss natoque penatibus et magn dis parturient montes,</p>
  </div>
  <div class="feature" style="left:437px">
    <div class="thumb" role="img" aria-label="Photo of a teacher with children at desks in a classroom" style="background:linear-gradient(180deg,#e8f0e0,#c9d9b8 50%,#8a7a6a)"></div>
    <h3>Teacher Feedback<br>&amp; Activities</h3>
    <p>Lorem ipsum dolor sit amet,sectetuer adipiscing elit. Aenean commodligula eget dolor. Aenean massa. C sociiss natoque penatibus et magn dis parturient montes,</p>
  </div>
  <div class="feature" style="left:647px">
    <div class="thumb" style="background:#fff">
      <svg width="193" height="108" viewBox="0 0 193 108" aria-label="Rising bar chart">
        <line x1="40" y1="8" x2="40" y2="96" stroke="#999"/>
        <line x1="40" y1="96" x2="185" y2="96" stroke="#999"/>
        <g fill="#c0392b">
          <rect x="48" y="86" width="8" height="10"/><rect x="60" y="82" width="8" height="14"/>
          <rect x="72" y="78" width="8" height="18"/><rect x="84" y="72" width="8" height="24"/>
          <rect x="96" y="66" width="8" height="30"/><rect x="108" y="58" width="8" height="38"/>
          <rect x="120" y="50" width="8" height="46"/><rect x="132" y="42" width="8" height="54"/>
          <rect x="144" y="34" width="8" height="62"/><rect x="156" y="26" width="8" height="70"/>
          <rect x="168" y="16" width="8" height="80"/>
        </g>
      </svg>
    </div>
    <h3>User Analytics</h3>
    <p>Lorem ipsum dolor sit amet,sectetuer adipiscing elit. Aenean commodligula eget dolor. Aenean massa. C sociiss natoque penatibus et magn dis parturient montes,</p>
  </div>
  <div class="more primary" style="left:34px"><span>Learn more</span><span>&gt;&gt;</span></div>
  <div class="more" style="left:247px"><span>Learn more</span><span>&gt;&gt;</span></div>
  <div class="more" style="left:453px"><span>Learn more</span><span>&gt;&gt;</span></div>
  <div class="more" style="left:666px"><span>Learn more</span><span>&gt;&gt;</span></div>
</section>

<section class="abs panel box feature-box">
  <div class="logo-slot">TechBuzz Daily</div>
  <h4>BrightNook featured in TechBuzz Daily</h4>
  <p>Lorem ipsum dolor sit asectetuer adipiscing elit. Aenean ommodligula eget dolor. Aeassa. C sociiss natoque penatibu</p>
</section>

<section class="abs panel box testimonial">
  <div class="pic" role="img" aria-label="Portrait photo of a smiling blonde woman" style="background:linear-gradient(180deg,#e8dcc8,#c8a878 50%,#4a4a4a)"></div>
  <h4>Testimonials</h4>
  <blockquote>Lorem ipsum dolor sit asectetuer ipiscing elit. Aenean ommodligula egetor. Aeassa. C sociiss natoque penatibuer ipiscing elit.</blockquote>
  <cite>- Marla, Mother of Two</cite>
</section>

<section class="abs panel apps">
  <svg class="arrow" style="left:14px" width="16" height="24" viewBox="0 0 16 24" aria-label="Previous"><path d="M13 2 3 12l10 10" fill="none" stroke="#aaa" stroke-width="4"/></svg>
  <div class="app" style="left:55px">
    <div class="icon" role="img" aria-label="App icon with an astronaut penguin" style="background:linear-gradient(#9fb6cf,#3e5f86)"></div>
    <div><b>This Weeks Words</b><span>by Simulark</span><span>FREE</span></div>
  </div>
  <div class="app" style="left:320px">
    <div class="icon" role="img" aria-label="App icon with a cartoon panda" style="background:linear-gradient(#f4f4f4,#cfe3b0)"></div>
    <div><b>Bamboo Word</b><span>by Bamboo Buddy</span><span>FREE</span></div>
  </div>
  <div class="app" style="left:572px">
    <div class="icon" role="img" aria-label="App icon with a cartoon owl" style="background:linear-gradient(#d9c8ee,#a98ad0)"></div>
    <div><b>Toddler Time</b><span>by Pixelfox Games</span><span>$1.99</span></div>
  </div>
  <svg class="arrow" style="left:821px" width="16" height="24" viewBox="0 0 16 24" aria-label="Next"><path d="M3 2l10 10L3 22" fill="none" stroke="#5fc01e" stroke-width="4"/></svg>
</section>

<p class="abs footer">Copyright © 2011, All Rights Reserved.</p>
<div class="abs social" style="left:828px;background:#3b5998" aria-label="Social link"></div>
<div class="abs social" style="left:862px;background:#3fb6e6" aria-label="Social link"></div>
</body>
</html>
```